Award-winnning Estate Agent needs a premium version of their 'For Sale' board design

We need a premium option for our 'For Sale' board design. We have a standard board that is attached to this brief, but were are looking to have a premium design version that we will use when selling exclusive properties. Our company name is Harbour Lane Estates and the name for this is exclusive selection is: 'The Harbour Collection'. The design needs to work with our current brand, but have a distinctive PREMIUM feel to it. I have uploaded the barnd guidelines and also some of the exisisting logo variations. We do NOT need a new logo but feel free to play around with colours, fonts, sizes etc. for the sign.

Target Market(s)

Property buyers & house hunters

Industry/Entity Type

Real Estate - Residential Property

Font styles to use
Sans Serif

Requirements
Must have
• A premium fee, must be square design, must be easy to read when driving past the sign
Nice to have
• I'm open ot ideas

```html
<!DOCTYPE html>
<html lang="en">
<head>
<meta charset="utf-8">
<title>Harbour Lane Estates – For Sale Board</title>
<link rel="stylesheet" href="https://fonts.googleapis.com/css2?family=Inter:wght@300;400;600;700&display=swap">
<style>
  :root {
    --board-dark: #38383b;
    --board-mid: #4d4d50;
    --board-light: #6f7073;
    --band-light: #cbccce;
    --band-dark: #3a3a3d;
    --ink-white: #ffffff;
    --ink-black: #0b0b0c;
    --font-main: "Inter", "Helvetica Neue", Arial, sans-serif;
  }
  * { margin: 0; padding: 0; box-sizing: border-box; }
  html, body {
    width: 1200px;
    height: 1200px;
    overflow: hidden;
    background: #ffffff;
  }
  .board {
    position: relative;
    width: 1200px;
    height: 1200px;
    font-family: var(--font-main);
    overflow: hidden;
  }
  .board__backdrop {
    position: absolute;
    inset: 0 0 284px 0;
    display: block;
  }
  .brand-name {
    position: absolute;
    top: 355px;
    left: 0;
    width: 100%;
    text-align: center;
    font-size: 46px;
    line-height: 1;
    font-weight: 600;
    color: var(--ink-white);
    letter-spacing: -0.01em;
  }
  .brand-rule {
    position: absolute;
    top: 432px;
    left: 106px;
    width: 982px;
    height: 3px;
    background: var(--ink-white);
  }
  .collection-title {
    position: absolute;
    top: 438px;
    left: 0;
    width: 100%;
    text-align: center;
    font-size: 102px;
    line-height: 1;
    font-weight: 300;
    color: var(--ink-white);
    letter-spacing: -0.02em;
  }
  .status {
    position: absolute;
    top: 690px;
    left: 0;
    width: 100%;
    text-align: center;
    font-size: 220px;
    line-height: 1;
    font-weight: 700;
    color: var(--ink-white);
    letter-spacing: -0.02em;
  }
  .phone-band {
    position: absolute;
    top: 916px;
    left: 0;
    width: 100%;
    height: 192px;
    background: var(--band-light);
    display: flex;
    justify-content: center;
    align-items: center;
    gap: 64px;
    font-size: 152px;
    font-weight: 400;
    color: var(--ink-black);
    letter-spacing: -0.01em;
    line-height: 1;
  }
  .web-band {
    position: absolute;
    top: 1108px;
    left: 0;
    width: 100%;
    height: 92px;
    background: var(--band-dark);
    display: flex;
    justify-content: center;
    align-items: center;
    font-size: 42px;
    font-weight: 300;
    color: var(--ink-white);
    letter-spacing: -0.01em;
  }
</style>
</head>
<body>
  <main class="board">
    <svg class="board__backdrop" width="1200" height="916" viewBox="0 0 1200 916" role="img" aria-label="Faint stylised townscape of a clock tower and rooftops behind the board text">
      <defs>
        <linearGradient id="boardShade" x1="0" y1="1" x2="1" y2="0">
          <stop offset="0" stop-color="var(--board-dark)"/>
          <stop offset="0.55" stop-color="var(--board-mid)"/>
          <stop offset="1" stop-color="var(--board-light)"/>
        </linearGradient>
      </defs>
      <rect width="1200" height="916" fill="url(#boardShade)"/>
    </svg>

    <p class="brand-name">Harbour Lane Estates</p>
    <div class="brand-rule"></div>
    <h1 class="collection-title">The Harbour Collection</h1>

    <p class="status">FOR SALE</p>

    <p class="phone-band"><span>01632</span><span>960418</span></p>

    <p class="web-band">www.harbourlaneestates.co.uk</p>
  </main>
</body>
</html>
```